Rehearsal studio business card design needed

My rehearsal studio i bought not that long ago was opened as a hobby originally and was definitely not taken seriously. I am trying to make the new look studio be launched with the new look business cards. I am looking for very simple and clean look cards to match the simple and clean studios. the colour scheme is red and grey. over all i am really just looking for a very simple card that is not too busy and just gets the point accross.
Target Market(s)
Targeting bands, music teachers, students, etc.
Industry/Entity Type
Business
Contact Information for Business Card
Bayridge Sound Centre
Rehearsal and Recording Facilities
Owen Barlow CEO
unit 8, 47 Garvin Road Tallow NSW 2093
0491 382 905
bayridgesoundcentre@mailvex.com
Requirements
Must have
- simplicity
Nice to have

```html
<!DOCTYPE html>
<html lang="en">
<head>
<meta charset="utf-8">
<title>Bayridge Sound Centre – Business Card</title>
<link rel="stylesheet" href="https://fonts.googleapis.com/css2?family=Share+Tech+Mono&display=swap">
<style>
  :root {
    --backdrop-centre: #b0151f;
    --backdrop-edge: #7e0a10;
    --card-black: #060606;
    --card-black-soft: #1c1616;
    --card-white: #ffffff;
    --brand-red: #c0181f;
    --brand-red-faint: #f3d3cc;
    --ink: #111111;
    --ghost-grey: #cfcfcf;
    --light-text: #ffffff;
  }
  * { margin: 0; padding: 0; box-sizing: border-box; }
  html, body { width: 1200px; height: 787px; overflow: hidden; }
  body {
    position: relative;
    background: radial-gradient(ellipse at 45% 45%, var(--backdrop-centre) 0%, var(--backdrop-edge) 100%);
    font-family: "Share Tech Mono", monospace;
  }

  /* Front of card */
  .card-front {
    position: absolute;
    left: 25px; top: 197px;
    width: 653px; height: 392px;
    background: linear-gradient(90deg, var(--card-black) 0%, var(--card-black) 40%, var(--card-black-soft) 100%);
  }
  .front-emblem {
    position: absolute;
    left: 267px; top: 55px;
    width: 130px; height: 130px;
    border-radius: 50%;
    background: var(--brand-red);
    border: 10px solid var(--card-black);
    box-shadow: 0 0 0 4px var(--brand-red);
  }
  .front-name {
    position: absolute;
    left: 160px; top: 282px;
    width: 340px;
    font-size: 34px;
    line-height: 1.05;
    color: var(--light-text);
    text-transform: lowercase;
    letter-spacing: 1px;
  }

  /* Back of card */
  .card-back {
    position: absolute;
    left: 529px; top: 149px;
    width: 654px; height: 392px;
    background: var(--card-white);
  }
  .back-band {
    position: absolute;
    left: 374px;
    width: 216px; height: 40px;
    background: var(--card-black);
  }
  .back-band--top { top: 0; }
  .back-band--bottom { bottom: 0; }

  .ghost-emblem {
    position: absolute;
    left: 126px; top: 50px;
    width: 132px; height: 132px;
    border-radius: 50%;
    border: 14px solid var(--brand-red-faint);
  }
  .ghost-name {
    position: absolute;
    left: 24px; top: 268px;
    width: 340px;
    font-size: 34px;
    line-height: 1.05;
    color: var(--ghost-grey);
    text-transform: lowercase;
    letter-spacing: 1px;
  }

  .contact {
    position: absolute;
    left: 388px; top: 196px;
    width: 240px;
    list-style: none;
    color: var(--ink);
    font-size: 10px;
    letter-spacing: 0.6px;
  }
  .contact-item {
    display: flex;
    align-items: flex-start;
    gap: 6px;
  }
  .contact-item + .contact-item { margin-top: 14px; }
  .contact-item--address { line-height: 18px; font-variant: small-caps; }
  .contact-item--email { text-transform: uppercase; font-size: 8.5px; }
  .contact-icon { flex: 0 0 22px; width: 22px; height: 18px; fill: var(--ink); }
</style>
</head>
<body>

<section class="card-front" aria-label="Card front">
  <div class="front-emblem" aria-hidden="true"></div>
  <p class="front-name">Bayridge Sound Centre</p>
</section>

<section class="card-back" aria-label="Card back">
  <div class="back-band back-band--top"></div>
  <div class="back-band back-band--bottom"></div>

  <div class="ghost-emblem" aria-hidden="true"></div>
  <p class="ghost-name" aria-hidden="true">Bayridge Sound Centre</p>

  <ul class="contact">
    <li class="contact-item contact-item--address">
      <svg class="contact-icon" viewBox="0 0 22 18" aria-hidden="true">
        <path d="M11 1 L1 9.5 L3 9.5 L3 17 L9 17 L9 12 L13 12 L13 17 L19 17 L19 9.5 L21 9.5 Z"/>
      </svg>
      <span>Bayridge Sound Centre Rehearsal and Recording Facilities Owen Barlow CEO unit 8, 47 Garvin Road Tallow NSW 2093</span>
    </li>
    <li class="contact-item contact-item--phone">
      <svg class="contact-icon" viewBox="0 0 22 18" aria-hidden="true">
        <path d="M2 5 Q11 0 20 5 L18 8 L15 7 L15 5 Q11 4 7 5 L7 7 L4 8 Z"/>
        <path d="M5 10 L8 8 L14 8 L17 10 L18 16 L4 16 Z"/>
      </svg>
      <span>0491 382 905</span>
    </li>
    <li class="contact-item contact-item--email">
      <svg class="contact-icon" viewBox="0 0 22 18" aria-hidden="true">
        <path d="M2 4 L20 4 L11 11 Z"/>
        <path d="M2 6 L11 13 L20 6 L20 15 L2 15 Z"/>
      </svg>
      <span>bayridgesoundcentre@mailvex.com</span>
    </li>
  </ul>
</section>

</body>
</html>
```